Willowmere Counseling (Endure - Mend - Flourish) - Double Sided Business Card

I would like a 2-sided business card. Front: Matte Black or Navy with Logo & Tagline. Back: Name, Address, Phone Number, Email, & Website (maybe would like to include a small map pin-pointing location); Prefer front to be a gold/silver foil (iridescent); Back prefer white or light colored background with lettering that is easy to read and simple

Target Market(s)

Individuals & Couples (13 y.o. - ALL Adults); High end clientele

Industry/Entity Type

Licensed Professional Counselor (Mental Health)

Contact Information for Business Card

Name: Willowmere Counseling; Tagline: Endure - Mend - Flourish; Address: 3870 N. Garrick Ave., Suite 214, Fort Worth, TX 76132; Phone: (214) 555-0187; Website: www.WillowmereCounseling.example

Font styles to use
Serif

Requirements
Must have
• Logo on Front (Large) prefer gold/silver foil on a matte dark color (i.e. black, navy, etc.); Back of Card: All other relevant information

```html
<!DOCTYPE html>
<html lang="en">
<head>
<meta charset="utf-8">
<title>Willowmere Counseling – Business Card</title>
<link rel="stylesheet" href="https://fonts.googleapis.com/css2?family=Cinzel:wght@400;600&family=Tinos:ital,wght@0,400;0,700;1,400&display=swap">
<style>
  :root {
    --backdrop: #e4ded4;
    --card-black: #050505;
    --card-white: #fbfbf9;
    --gold: #d4ad2f;
    --gold-line: #c9a11f;
    --silver: #9a9a9c;
    --ink: #2b2b2b;
    --icon-disc: #2f3237;
  }
  * { margin: 0; padding: 0; box-sizing: border-box; }
  html, body { width: 1200px; height: 800px; overflow: hidden; }
  body {
    background: var(--backdrop);
    display: flex;
    align-items: center;
    justify-content: center;
    gap: 40px;
  }
  .card {
    position: relative;
    width: 530px;
    height: 303px;
    overflow: hidden;
    box-shadow: 0 12px 30px rgba(0,0,0,0.18);
  }

  /* Front */
  .card-front { background: var(--card-black); }
  .front-brand {
    position: absolute;
    left: 0; right: 0; top: 62px;
    display: flex; flex-direction: column; align-items: center;
  }
  .brand-disc {
    width: 54px; height: 54px;
    border-radius: 50%;
    border: 3px solid var(--gold);
    margin-bottom: 14px;
  }
  .brand-name {
    font-family: 'Cinzel', serif;
    font-weight: 600;
    color: var(--gold);
    font-size: 27px;
    letter-spacing: 1px;
  }
  .brand-tagline {
    margin-top: 10px;
    font-family: 'Cinzel', serif;
    font-weight: 400;
    color: var(--gold);
    font-size: 12px;
    letter-spacing: 1.5px;
  }
  .front-rule {
    position: absolute;
    left: 0; right: 0; top: 228px;
    height: 2px;
    background: var(--gold-line);
  }

  /* Back */
  .card-back { background: var(--card-white); }
  .back-brand {
    position: absolute;
    left: 30px; top: 38px;
    width: 170px;
    display: flex; flex-direction: column; align-items: center; gap: 10px;
  }
  .back-brand .brand-disc { width: 46px; height: 46px; margin: 0; border-color: var(--gold); }
  .back-brand .brand-name { font-size: 17px; text-align: center; line-height: 1.25; }
  .back-rule-left {
    position: absolute;
    left: 0; top: 148px;
    width: 210px; height: 2px;
    background: var(--gold-line);
  }
  .back-rule-right {
    position: absolute;
    right: 0; top: 262px;
    width: 44px; height: 2px;
    background: var(--gold-line);
  }
  .holder {
    position: absolute;
    left: 270px; top: 48px;
    font-family: 'Tinos', serif;
    color: var(--ink);
  }
  .holder-name { font-weight: 700; font-size: 19px; letter-spacing: 0.5px; }
  .holder-title { font-style: italic; font-size: 16px; margin-top: 1px; }
  .contact-list {
    position: absolute;
    left: 222px; top: 128px;
    list-style: none;
    font-family: 'Tinos', serif;
    color: var(--ink);
    font-size: 12.5px;
  }
  .contact-item {
    display: flex; align-items: center; gap: 10px;
    min-height: 30px; margin-bottom: 6px;
  }
  .contact-icon {
    flex: 0 0 26px; width: 26px; height: 26px;
    border-radius: 50%;
    background: var(--icon-disc);
    display: flex; align-items: center; justify-content: center;
  }
  .contact-icon svg { width: 14px; height: 14px; fill: none; stroke: #fff; stroke-width: 1.6; stroke-linecap: round; stroke-linejoin: round; }
  .contact-text { line-height: 1.2; }
</style>
</head>
<body>

  <section class="card card-front" aria-label="Card front">
    <div class="front-brand">
      <span class="brand-disc"></span>
      <span class="brand-name">WILLOWMERE COUNSELING</span>
      <span class="brand-tagline">ENDURE - MEND - FLOURISH</span>
    </div>
    <div class="front-rule"></div>
  </section>

  <section class="card card-back" aria-label="Card back">
    <div class="back-brand">
      <span class="brand-disc"></span>
      <span class="brand-name">Willowmere Counseling</span>
    </div>
    <div class="back-rule-left"></div>

    <div class="holder">
      <p class="holder-name">YOUR NAME</p>
      <p class="holder-title">Manager</p>
    </div>

    <ul class="contact-list">
      <li class="contact-item">
        <span class="contact-icon"><svg viewBox="0 0 24 24"><path d="M5 3h4l2 5-2.5 1.5a11 11 0 0 0 6 6L16 13l5 2v4a2 2 0 0 1-2 2A16 16 0 0 1 3 5a2 2 0 0 1 2-2z"/></svg></span>
        <span class="contact-text">(214) 555-0187</span>
      </li>
      <li class="contact-item">
        <span class="contact-icon"><svg viewBox="0 0 24 24"><path d="M12 22s7-7 7-12a7 7 0 0 0-14 0c0 5 7 12 7 12z"/><circle cx="12" cy="10" r="2.5"/></svg></span>
        <span class="contact-text">3870 N. Garrick Ave., Suite 214,<br>Fort Worth, TX 76132</span>
      </li>
      <li class="contact-item">
        <span class="contact-icon"><svg viewBox="0 0 24 24"><circle cx="12" cy="12" r="9"/><path d="M3 12h18M12 3a14 14 0 0 1 0 18M12 3a14 14 0 0 0 0 18"/></svg></span>
        <span class="contact-text">www.WillowmereCounseling.example</span>
      </li>
      <li class="contact-item">
        <span class="contact-icon"><svg viewBox="0 0 24 24"><circle cx="12" cy="12" r="3.5"/><path d="M15.5 12v1.5a2.5 2.5 0 0 0 5 0V12a8.5 8.5 0 1 0-3.5 6.9"/></svg></span>
        <span class="contact-text">info@WillowmereCounseling.example</span>
      </li>
    </ul>
    <div class="back-rule-right"></div>
  </section>

</body>
</html>
```